Tolvane Vitamins Sign

I need to make a sign that looks like a vintage metal sign like you would find in an old pharmacy. I'm attaching a few examples of the look and feel. The text is attached in the word file

```html
<!DOCTYPE html>
<html lang="en">
<head>
<meta charset="utf-8">
<title>Tolvane Vitamins Sign</title>
<link rel="stylesheet" href="https://fonts.googleapis.com/css2?family=Rye&display=swap">
<style>
  :root {
    --frame-teal: #7fa8a3;
    --panel-teal: #22434a;
    --ornament-teal: rgba(127, 168, 163, 0.16);
    --sign-white: #f3f7f3;
    --sign-red: #b8503e;
    --line-teal: #7fa8a3;
  }
  html, body {
    margin: 0;
    padding: 0;
    overflow: hidden;
    background: var(--frame-teal);
  }
  .sign {
    position: relative;
    width: 1200px;
    height: 1002px;
    background: var(--frame-teal);
    overflow: hidden;
  }
  .sign-panel {
    position: absolute;
    left: 18px;
    top: 16px;
    right: 18px;
    bottom: 18px;
    background: var(--panel-teal);
    border-radius: 4px;
  }
  .ornament {
    position: absolute;
    background: var(--ornament-teal);
    border-radius: 40px;
  }
  .ornament--top-left { left: 55px; top: 38px; width: 480px; height: 110px; }
  .ornament--top-right { right: 55px; top: 38px; width: 480px; height: 110px; }
  .ornament--left-upper { left: 50px; top: 150px; width: 90px; height: 240px; }
  .ornament--right-upper { right: 50px; top: 150px; width: 90px; height: 240px; }
  .ornament--left-lower { left: 50px; top: 590px; width: 90px; height: 260px; }
  .ornament--right-lower { right: 50px; top: 590px; width: 90px; height: 260px; }
  .ornament--bottom-left { left: 55px; bottom: 40px; width: 480px; height: 110px; }
  .ornament--bottom-right { right: 55px; bottom: 40px; width: 480px; height: 110px; }
  .ornament--scroll-top { left: 500px; top: 122px; width: 200px; height: 36px; }
  .ornament--scroll-bottom { left: 500px; top: 815px; width: 200px; height: 36px; }

  .rule {
    position: absolute;
    left: 395px;
    width: 417px;
    height: 2px;
    background: var(--line-teal);
  }
  .rule--top { top: 159px; }
  .rule--bottom { top: 811px; }

  .tagline {
    position: absolute;
    left: 0;
    width: 1200px;
    text-align: center;
    font-family: "Rye", serif;
    color: var(--frame-teal);
    margin: 0;
    line-height: 1;
  }
  .tagline--since { top: 175px; font-size: 44px; letter-spacing: 2px; }
  .tagline--history { top: 733px; font-size: 46px; letter-spacing: 3px; }

  .brand-name {
    position: absolute;
    left: 0;
    width: 1200px;
    margin: 0;
    text-align: center;
    font-family: "Rye", serif;
    font-weight: 400;
    color: var(--sign-white);
    line-height: 1;
    -webkit-text-stroke: 3px var(--sign-red);
    paint-order: stroke fill;
    text-shadow: -5px 5px 0 var(--sign-red), -9px 9px 0 rgba(184, 80, 62, 0.75), -13px 13px 0 rgba(184, 80, 62, 0.5);
  }
  .brand-name__line {
    display: block;
    font-size: 196px;
  }
  .brand-name__line--first { margin-top: 0; }
  .brand-name__line--second { margin-top: 12px; font-size: 200px; }
</style>
</head>
<body>
<main class="sign">
  <div class="sign-panel"></div>

  <div class="ornament ornament--top-left" role="img" aria-label="Engraved leaf scroll ornament, top left corner"></div>
  <div class="ornament ornament--top-right" role="img" aria-label="Engraved leaf scroll ornament, top right corner"></div>
  <div class="ornament ornament--left-upper" role="img" aria-label="Engraved leaf scroll ornament along the upper left edge"></div>
  <div class="ornament ornament--right-upper" role="img" aria-label="Engraved leaf scroll ornament along the upper right edge"></div>
  <div class="ornament ornament--left-lower" role="img" aria-label="Engraved leaf scroll ornament along the lower left edge"></div>
  <div class="ornament ornament--right-lower" role="img" aria-label="Engraved leaf scroll ornament along the lower right edge"></div>
  <div class="ornament ornament--bottom-left" role="img" aria-label="Engraved leaf scroll ornament, bottom left corner"></div>
  <div class="ornament ornament--bottom-right" role="img" aria-label="Engraved leaf scroll ornament, bottom right corner"></div>
  <div class="ornament ornament--scroll-top" role="img" aria-label="Small curled scroll flourish above the heading"></div>
  <div class="ornament ornament--scroll-bottom" role="img" aria-label="Small curled scroll flourish below the tagline"></div>

  <div class="rule rule--top"></div>
  <p class="tagline tagline--since">Since 70,000 BCE</p>

  <h1 class="brand-name" style="top:250px;">
    <span class="brand-name__line brand-name__line--first">Tolvane</span>
    <span class="brand-name__line brand-name__line--second">Vitamins</span>
  </h1>

  <p class="tagline tagline--history">history of humankind</p>
  <div class="rule rule--bottom"></div>
</main>
</body>
</html>
```